Business Card Design, including supply of raw art files plus a vector diagram of the zelvon logo and

We need the business card design for a company that is launching a new exciting product. The brief requires the submission of the following once the final design is chosen:

- business card layout including raw files
- a composite vector image file of the zelvon logo and tag line
- a standalone vector image file of the zelvon logo

The product will be launched as a customer engagement app.

It has 4 core modules which enables a person to do multiple things - book tours and activities, order takeaways, search for local deals and offers. A universal currency is at the heart of this product. When you use the app, you earn cashback rewards when shopping or buying at any of the merchant partners across the modules as . These rewards can then be used as full or part payment when buying goods or services at these merchant partners.

The business card must help us build the brand, communicate the benefit of the brand's key focus - the ability to earn and burn this universal cashback ccurrency - across the 4 modules - booking of tours and activities, ordering, searching for local deals and payment.

We would like the design to use the brand's blue colour the hex colour is: 00
Dark grey : 646464
Darker blue shadow: 058bdd
Main Blue: 0084ff

We need to translate this into a CMYK print or spot colour print.

Both print options to be supplied as separate files.

An example of the base concept we have in mind is attached for your reference.

The font used by the brand is Proxima Nova.

Note: the duration has been set as 2 days.

Industry/Entity Type

Business

Contact Information for Business Card

Carla Mendoza
Marketing
W: www.zelvon.example
M: + 61 400555123
T: +61 2 5550 1473
A: Suite 7, Level 2, 14-18 Harwick Street, Sydney, NSW, 2000, Australia

Font styles to use
Sans Serif

Requirements
Must have
• zelVon logo and tagline
• address details
• zelVon icons as supplied
Nice to have
• would like to have the option of a spot varnish layer over the logo and icons at the back of the card

```html
<!DOCTYPE html>
<html lang="en">
<head>
<meta charset="utf-8">
<title>zelVon business card</title>
<link rel="stylesheet" href="https://fonts.googleapis.com/css2?family=Source+Sans+3:wght@300;400;600;700&display=swap">
<style>
  :root {
    --stage: #3a3a3c;
    --brand-blue: #3188c9;
    --paper: #ffffff;
    --ink-grey: #5f5f61;
    --name-blue: #2f86c8;
  }
  html, body {
    margin: 0;
    width: 1200px;
    height: 1200px;
    overflow: hidden;
    background: var(--stage);
    font-family: "Source Sans 3", "Helvetica Neue", Arial, sans-serif;
  }
  .card {
    position: absolute;
    left: 180px;
    width: 840px;
    height: 480px;
    display: block;
  }
  .card--front { top: 96px; background: var(--brand-blue); }
  .card--back  { top: 624px; background: var(--paper); }
  .wordmark { font-weight: 300; fill: var(--paper); }
  .tagline  { font-weight: 300; fill: var(--paper); }
  .module-icon { fill: var(--paper); }
  .module-divider { stroke: var(--paper); stroke-width: 3; }
  .person-name { font-weight: 700; fill: var(--name-blue); }
  .person-role { font-weight: 400; fill: var(--ink-grey); }
  .contact-text { font-weight: 400; fill: var(--ink-grey); }
  .contact-badge { fill: var(--name-blue); }
  .contact-glyph { fill: var(--paper); }
  .contact-glyph-line { stroke: var(--paper); fill: none; stroke-width: 1.4; }
</style>
</head>
<body>

<svg class="card card--front" viewBox="0 0 840 480" aria-label="Card front">
  <circle cx="293" cy="188" r="62" fill="#ffffff"/>
  <text class="wordmark" x="376" y="208" font-size="100">zelVon</text>
  <text class="tagline" x="656" y="235" font-size="25" text-anchor="end">the cloud currency</text>

  <!-- module icons -->
  <g class="module-icon">
    <!-- camera -->
    <path d="M246 354 h14 l6 -9 h20 l6 9 h16 a6 6 0 0 1 6 6 v28 a6 6 0 0 1 -6 6 h-62 a6 6 0 0 1 -6 -6 v-28 a6 6 0 0 1 6 -6z M280 357 a15 15 0 1 0 0.01 0z M280 363 a9 9 0 1 1 -0.01 0z" fill-rule="evenodd"/>
    <circle cx="304" cy="357" r="2.5" fill="#3188c9"/>
    <!-- exchange -->
    <path d="M360 345 l14 0 l-4 4 a20 20 0 0 1 16 6 l-6 4 a13 13 0 0 0 -14 -3 l4 5 z"/>
    <circle cx="384" cy="369" r="12"/>
    <text x="384" y="375" font-size="17" font-weight="700" text-anchor="middle" fill="#3188c9">$</text>
    <path d="M410 392 l-14 0 l4 -4 a20 20 0 0 1 -16 -6 l6 -4 a13 13 0 0 0 14 3 l-4 -5 z"/>
    <!-- cutlery -->
    <path d="M444 344 l40 46 l-3 3 l-40 -46 z"/>
    <path d="M442 344 l4 8 M447 342 l4 8 M452 341 l3 9" stroke="#fff" stroke-width="2"/>
    <ellipse cx="478" cy="350" rx="7" ry="10" transform="rotate(40 478 350)"/>
    <path d="M473 356 l-30 35 l3 3 l30 -35 z"/>
    <!-- tag -->
    <path d="M570 342 h24 v24 l-28 28 l-24 -24 z M585 349 a4 4 0 1 0 0.01 0z" fill-rule="evenodd"/>
  </g>
  <line class="module-divider" x1="337" y1="345" x2="337" y2="390"/>
  <line class="module-divider" x1="427" y1="345" x2="427" y2="390"/>
  <line class="module-divider" x1="518" y1="345" x2="518" y2="390"/>
</svg>

<svg class="card card--back" viewBox="0 0 840 480" aria-label="Card back">
  <text class="person-name" x="266" y="126" font-size="38">CARLA MENDOZA</text>
  <text class="person-role" x="355" y="156" font-size="26">marketing</text>

  <!-- address -->
  <circle class="contact-badge" cx="284" cy="261" r="21"/>
  <path class="contact-glyph" d="M284 252 a6 6 0 0 1 6 6 c0 4 -6 11 -6 11 c0 0 -6 -7 -6 -11 a6 6 0 0 1 6 -6z M284 256 a2 2 0 1 0 0.01 0z" fill-rule="evenodd"/>
  <text class="contact-text" x="334" y="264" font-size="22">Suite 7, Level 2, 14-18 Harwick Street,</text>
  <text class="contact-text" x="334" y="294" font-size="22">Sydney, NSW, 2000, Australia</text>

  <!-- phone -->
  <circle class="contact-badge" cx="284" cy="334" r="21"/>
  <rect class="contact-glyph" x="278" y="322" width="12" height="22" rx="2"/>
  <rect x="280" y="325" width="8" height="14" fill="#2f86c8"/>
  <text class="contact-text" x="334" y="338" font-size="22">+ 61 400555123</text>
  <text class="contact-text" x="334" y="367" font-size="22">+61 2 5550 1473</text>

  <!-- web -->
  <circle class="contact-badge" cx="284" cy="410" r="21"/>
  <g class="contact-glyph-line">
    <circle cx="284" cy="410" r="9"/>
    <ellipse cx="284" cy="410" rx="4" ry="9"/>
    <line x1="275" y1="410" x2="293" y2="410"/>
    <line x1="276" y1="405" x2="292" y2="405"/>
    <line x1="276" y1="415" x2="292" y2="415"/>
  </g>
  <text class="contact-text" x="334" y="420" font-size="22">W: www.zelvon.example</text>
</svg>

</body>
</html>
```